Updated website design needed for Radiology Group, Pinecrest Valley Imaging Partners

Clean, uncluttered, updated design needed for top regional Radiology Center. Focus on personal, patient oriented design, (not clinical). Should be simple and easy to navigate, with clear CTAs. Use blues, greens and photos of people in the Central Oregon outdoors.
Uncoded, PSD design only. 2 pages: Home page and one example interior page.
reference current site: http://www.pvipxq.com/
Sites they like:
http://www.hollowbrookscan.com/
http://www.mdlq.net/handler.cfm?event=practice,main
http://www.elmtidejoint.com/

Industry/Entity Type

Medical Imaging

Number of Pages Required

2 page

Font styles to use
Sans Serif

Requirements
Must have
• Personal and patient friendly.
• Lots of white space, clean and uncluttered. Clear CTAs, such as: Patient Bill Pay, Make an Appointment, Meet Our Doctors
• Use copy and contact information from the current site.
• Use outdoor images from Central Oregon, late Winter/ Spring (snow, light colors, spring green, for example)
• Include one example interior page, either Your Exam or Meet Our Doctors
Nice to have
• The client likes:
• Meet Our Doctors slider section, and big, easy to navigate Information Center on www.elmtidejoint.com
• The personal feel of the Your Exam section on www.hollowbrookscan.com
• Blues and Greens, outdoorsy imagery
Should not have
• The client does not like:
• complex drop down menus
• clinical feel
• Do not use lorum ipsum or dummy text.
• Do not use outdoor images from other regions. Do not use Summer (hot, poolside) or Fall (red/orange leaves) images.

```html
<!DOCTYPE html>
<html lang="en">
<head>
<meta charset="utf-8">
<title>Pinecrest Valley Imaging Partners</title>
<link href="https://fonts.googleapis.com/css2?family=Raleway:wght@500;600;700;800&family=Open+Sans:wght@400;600&family=DM+Serif+Display&display=swap" rel="stylesheet">
<style>
:root{
  --blue:#2a87e8;
  --blue-deep:#2466c9;
  --green:#1fcf72;
  --ink:#444;
  --muted:#777;
  --soft:#f5f6f9;
  --line:#d8dbe0;
  --white:#fff;
}
*{margin:0;padding:0;box-sizing:border-box}
html,body{width:703px;height:1200px;overflow:hidden;background:var(--white)}
body{position:relative;font-family:"Open Sans",Arial,sans-serif;color:var(--ink)}
.abs{position:absolute}
a{color:inherit;text-decoration:none}

/* header */
.brand{left:52px;top:5px;height:29px;display:flex;align-items:center;gap:5px}
.brand-mark{width:27px;height:29px;background:#8f9bc4}
.brand-name{font-family:"Open Sans",sans-serif;font-size:7.5px;line-height:9px;color:#333;width:72px}
.cta{top:7px;height:24px;width:100px;border:1px solid var(--line);border-radius:2px;font:600 6.6px "Open Sans",sans-serif;color:#8a8a8a;display:flex;align-items:center;justify-content:center;letter-spacing:.2px}
.cta.primary{background:var(--green);border-color:var(--green);color:var(--white)}

.nav{left:0;top:39px;width:703px;height:33px;background:var(--blue)}
.nav ul{list-style:none;display:flex;position:absolute;left:52px;top:0;height:33px}
.nav li{font:600 6.8px "Open Sans",sans-serif;color:var(--white);height:33px;display:flex;align-items:center;margin-right:15.6px}
.nav li.active{border-bottom:2px solid var(--white);padding:0 9px;margin-left:0;font-weight:700}

/* hero */
.hero{left:0;top:72px;width:703px;height:252px;background:linear-gradient(100deg,#f1f1f1 0%,#dedede 40%,#c9c9c9 62%,#e9e9e9 100%)}
.hero-figure{left:330px;top:40px;width:170px;height:212px;background:linear-gradient(180deg,#8e8e8e,#5a5a5a);border-radius:80px 80px 0 0}
.hero-title{left:52px;top:145px;font:800 32px/1 "Raleway",sans-serif;color:var(--blue);letter-spacing:-.5px}
.hero-title span{color:var(--ink)}
.hero-sub{left:52px;top:182px;font:700 15.6px/1 "Raleway",sans-serif;color:var(--ink)}
.hero-btn{left:52px;top:211px;width:82px;height:24px;border-radius:12px;background:var(--blue);color:var(--white);font:600 6.8px "Open Sans",sans-serif;display:flex;align-items:center;justify-content:center}
.dot{left:674px;width:5px;height:5px;border-radius:50%;background:#444}
.dot.on{background:var(--blue)}

/* section index */
.index-num{font:400 33px/1 "DM Serif Display",serif;color:var(--blue)}
.index-line{width:1px;background:var(--blue)}
.index-label{writing-mode:vertical-rl;transform:rotate(180deg);font:600 6.3px "Open Sans",sans-serif;color:var(--blue);letter-spacing:.3px}

/* services */
.services-photo{left:185px;top:344px;width:138px;height:223px;background:linear-gradient(180deg,#e4ecf5 0%,#2f6fcf 45%,#2457b4 100%);border-radius:60px 60px 0 0}
.section-title{font:700 15.6px/1 "Raleway",sans-serif;color:var(--blue)}
.section-kicker{font:400 6.6px "Open Sans",sans-serif;color:var(--ink)}
.rule{height:2px;width:23px;background:var(--blue)}
.services-copy{left:398px;top:410px;width:252px;font:400 6.7px/13px "Open Sans",sans-serif;color:#666}
.services-copy p+p{margin-top:3px}

/* reviews */
.reviews{left:0;top:567px;width:703px;height:213px;background:var(--soft)}
.review-card{top:636px;width:222px;height:89px;background:var(--white);box-shadow:0 2px 0 #e3e6ea}
.quote{position:absolute;left:17px;top:13px}
.review-text{position:absolute;left:17px;top:33px;width:190px;font:400 6.7px/13px "Open Sans",sans-serif;color:#8a8a8a}
.avatar{top:711px;width:42px;height:42px;border-radius:50%;border:2px solid var(--white)}

/* doctors */
.doc-back{left:138px;top:823px;width:279px;height:170px;background:linear-gradient(90deg,#9aa3b1,#c7ccd3 50%,#9aa3b1)}
.doc-front{left:183px;top:811px;width:184px;height:188px;background:linear-gradient(180deg,#7c8087 0%,#8e939b 55%,#c9b8bd 100%)}
.doc-facts{right:52px;top:864px;width:240px;text-align:right;font:400 8.3px/15.6px "Open Sans",sans-serif;color:#666}
.read-more{right:52px;top:979px;font:700 6.8px "Open Sans",sans-serif;color:var(--blue);letter-spacing:.2px}

/* footer */
.footer{left:0;top:1029px;width:703px;height:148px;background:var(--blue);color:var(--white)}
.foot-col{top:1044px}
.foot-col h4{font:600 7.8px "Raleway",sans-serif;letter-spacing:.1px;margin-bottom:7px}
.foot-col ul{list-style:none}
.foot-col li{font:400 6.8px/13px "Open Sans",sans-serif;padding-left:7px;position:relative}
.foot-col li::before{content:"";position:absolute;left:0;top:7px;width:2.5px;height:2.5px;border:0.7px solid var(--white);border-radius:50%}
.contact li{padding-left:12px;line-height:18.2px}
.contact li::before{display:none}
.contact svg{position:absolute;left:0;top:6px}
.copyright{left:0;top:1177px;width:703px;height:23px;background:var(--blue-deep);color:var(--white);font:400 6.6px/23px "Open Sans",sans-serif;text-align:center}
</style>
</head>
<body>

<!-- header -->
<div class="abs brand"><span class="brand-mark"></span><span class="brand-name">Pinecrest Valley Imaging Partners</span></div>
<a class="abs cta" style="left:345px">MEET OUR DOCTORS</a>
<a class="abs cta" style="left:448px">PATIENT BILL PAY</a>
<a class="abs cta primary" style="left:550px">MAKE AN POOINTMENT</a>

<nav class="abs nav">
  <ul>
    <li class="active">HOME</li>
    <li>ABOUT US</li>
    <li>OUR SERVICES</li>
    <li>FOR PATIENTS</li>
    <li>OUR PHYSICIANS</li>
    <li>FOR PHYSICIANS</li>
    <li>PACS &amp; DOCUMENTS</li>
    <li>APPOINTMENTS</li>
    <li>OUR LOCATIONS</li>
  </ul>
</nav>

<!-- hero -->
<section class="abs hero" role="img" aria-label="Black and white photo of a woman looking over a snowy mountain landscape">
  <div class="abs hero-figure"></div>
</section>
<h1 class="abs hero-title">WELCOME <span>TO</span></h1>
<p class="abs hero-sub">PINECREST VALLEY IMAGING</p>
<a class="abs hero-btn">LEARN MORE</a>
<span class="abs dot on" style="top:185px"></span>
<span class="abs dot" style="top:196px"></span>
<span class="abs dot" style="top:206px"></span>

<!-- services -->
<div class="abs index-num" style="left:55px;top:388px">01</div>
<div class="abs index-line" style="left:73px;top:427px;height:39px"></div>
<div class="abs index-label" style="left:70px;top:473px">WHAT WE DO</div>
<div class="abs services-photo" role="img" aria-label="Photo of a doctor in blue scrubs and surgical cap with arms crossed"></div>
<h2 class="abs section-title" style="left:398px;top:362px">SERVICES</h2>
<div class="abs section-kicker" style="left:398px;top:381px">WHAT WE DO</div>
<div class="abs rule" style="left:398px;top:396px"></div>
<div class="abs services-copy">
  <p>Pinecrest Valley Imaging Partners is a diagnostic imaging corporation providing professional services to Central and Eastern Oregon hospitals and clinics as well as state-of-the-art services in its’ own outpatient imaging center. PVIP was established by its’ founder, Harold W. Brenner, MD when he opened his Central Oregon practice in 1947.</p>
  <p>PVIP is staffed by fellowship trained physicians with expertise in major disciplines to include mammography, ultrasound, Magnetic Resonance Imaging, Computed Tomography, Positron Emission Tomography, interventional procedures, Nuclear Medicine and general procedures which include fluoroscopy, tomography...</p>
</div>

<!-- reviews -->
<section class="abs reviews"></section>
<h2 class="abs section-title" style="left:52px;top:596px">CLIENT REVIEWS</h2>
<div class="abs rule" style="left:52px;top:617px"></div>
<svg class="abs" style="left:537px;top:598px" width="20" height="10" viewBox="0 0 20 10"><path d="M5 1 1 5l4 4" fill="none" stroke="#2a87e8" stroke-width="1.4"/><path d="M15 1l4 4-4 4" fill="none" stroke="#333" stroke-width="1.4"/></svg>
<div class="abs index-num" style="left:613px;top:602px">02</div>
<div class="abs index-line" style="left:632px;top:643px;height:37px"></div>
<div class="abs index-label" style="left:629px;top:687px">THE CLIENT LIKES</div>

<div class="abs review-card" style="left:56px">
  <svg class="quote" width="13" height="10" viewBox="0 0 13 10"><path d="M5 0C2 1 0 3 0 6a3 3 0 1 0 3-2c0-2 1-3 2.6-3.6zM12 0C9 1 7 3 7 6a3 3 0 1 0 3-2c0-2 1-3 2.6-3.6z" fill="#2a87e8"/></svg>
  <p class="review-text">I couldn't believe how smoothly it went. I'm a new man. It's wonderful to have all that freedom without pain anymore.</p>
</div>
<div class="abs avatar" style="left:52px;background:linear-gradient(135deg,#e9ecef,#b7bcc3)" role="img" aria-label="Portrait photo of a reviewer in a white coat"></div>

<div class="abs review-card" style="left:332px">
  <svg class="quote" width="13" height="10" viewBox="0 0 13 10"><path d="M5 0C2 1 0 3 0 6a3 3 0 1 0 3-2c0-2 1-3 2.6-3.6zM12 0C9 1 7 3 7 6a3 3 0 1 0 3-2c0-2 1-3 2.6-3.6z" fill="#1fcf72"/></svg>
  <p class="review-text">I couldn't believe how smoothly it went. I'm a new man. It's wonderful to have all that freedom without pain anymore.</p>
</div>
<div class="abs avatar" style="left:325px;background:linear-gradient(135deg,#d8cfc8,#8a7468)" role="img" aria-label="Portrait photo of a smiling woman reviewer"></div>

<!-- doctors -->
<div class="abs index-num" style="left:52px;top:825px">03</div>
<div class="abs index-line" style="left:70px;top:864px;height:38px"></div>
<div class="abs index-label" style="left:67px;top:911px">MEET OUR DOCTORS</div>
<div class="abs doc-back" role="img" aria-label="Faded photos of neighbouring doctors in the slider"></div>
<div class="abs doc-front" role="img" aria-label="Portrait photo of a radiologist in a checked shirt"></div>
<svg class="abs" style="left:163px;top:901px" width="6" height="10" viewBox="0 0 6 10"><path d="M5 1 1 5l4 4" fill="none" stroke="#fff" stroke-width="1.4"/></svg>
<svg class="abs" style="left:381px;top:901px" width="6" height="10" viewBox="0 0 6 10"><path d="M1 1l4 4-4 4" fill="none" stroke="#fff" stroke-width="1.4"/></svg>
<h2 class="abs section-title" style="right:52px;top:830px">MEET OUR DOTORS</h2>
<div class="abs rule" style="left:628px;top:851px"></div>
<div class="abs doc-facts">
  Specialty – Body Imaging, Diagnostic Radiology<br>
  Certifications – National Board of Imaging 2005 and<br>
  Vascular Interpretation 2006<br>
  Medical School – Lakeshore Medical College, 2000<br>
  Residency – Eastmoor University, 2005<br>
  Fellowship – Abdominal Imaging, Lakeshore University,<br>
  2006
</div>
<a class="abs read-more">READ MORE</a>

<!-- footer -->
<footer class="abs footer"></footer>
<div class="abs foot-col" style="left:52px;color:#fff">
  <h4>FOR PATIENTS</h4>
  <ul><li>About Your Visit</li><li>Why Choose Us?</li><li>Patient Forms</li><li>Billing and Insurance</li><li>Locations and Maps</li><li>Appointments</li></ul>
</div>
<div class="abs foot-col" style="left:219px;color:#fff">
  <h4>FOR PATIENTS</h4>
  <ul><li>Home</li><li>About Us</li><li>Our Physicians</li><li>For Physicians</li><li>Disclaimer</li><li>HIPAA</li><li>Log-In</li></ul>
</div>
<div class="abs foot-col" style="left:375px;color:#fff">
  <h4>FOR PATIENTS</h4>
  <ul><li>Our Services</li><li>Mammography</li><li>MRI</li><li>CT-64</li><li>X-Ray</li><li>Nuclear Medicine</li><li>PET</li><li>Ultrasound</li></ul>
</div>
<div class="abs foot-col contact" style="left:531px;color:#fff">
  <h4>CONTACT US</h4>
  <ul>
    <li><svg width="6" height="6" viewBox="0 0 6 6"><path d="M1 0.5 2.2 0.3 2.8 1.8 2 2.4Q2.6 3.6 3.6 4L4.2 3.2 5.7 3.8 5.5 5Q2.5 5.6 0.5 1.2Z" fill="#fff"/></svg>(555) 210-4630 - Main Line</li>
    <li><svg width="6" height="6" viewBox="0 0 6 6"><rect x=".5" y="1" width="5" height="4.5" fill="none" stroke="#fff" stroke-width=".8"/><path d="M.5 2.4h5" stroke="#fff" stroke-width=".8"/></svg>(555) 210-4788 - Scheduling</li>
    <li><svg width="7" height="6" viewBox="0 0 7 6"><rect x=".4" y="1" width="6.2" height="4" fill="none" stroke="#fff" stroke-width=".8"/><path d="M.4 2.4h6.2" stroke="#fff" stroke-width="1"/></svg>(555) 210-5912 - Billing</li>
    <li><svg width="6" height="7" viewBox="0 0 6 7"><rect x=".6" y=".5" width="4.8" height="6" fill="none" stroke="#fff" stroke-width=".8"/><path d="M1.8 2.2h2.4M1.8 3.5h2.4M1.8 4.8h2.4" stroke="#fff" stroke-width=".6"/></svg>(555) 210-6075 - Medical Records</li>
  </ul>
</div>
<div class="abs copyright">© 2016 Pinecrest Valley Imaging Partners</div>

</body>
</html>
```